MP7 (acronym stands for Mealport 7)

We are a sales and marketing start up. We sell bar and beverage dispensing equipment presently and we will add foodservice equipment to our portfolio in the coming year. We like our logo but we will consider different presentations of "MP7"

Industry/Entity Type

Marketing

```html
<!DOCTYPE html>
<html lang="en">
<head>
<meta charset="utf-8">
<title>MP7 Food Service Representation – Business Card</title>
<link rel="stylesheet" href="https://fonts.googleapis.com/css2?family=Arimo:wght@400;700&family=Alegreya+SC:wght@800&family=Pinyon+Script&display=swap">
<style>
  :root {
    --paper: #ffffff;
    --ink: #111111;
    --ink-soft: #333333;
    --crop: #000000;
    --flag-red: #d52b1e;
    --flag-white: #f4f4f4;
  }
  html, body {
    margin: 0;
    padding: 0;
    width: 1200px;
    height: 750px;
    overflow: hidden;
    background: var(--paper);
  }
  .card {
    position: relative;
    width: 1200px;
    height: 750px;
    background: var(--paper);
    color: var(--ink);
    overflow: hidden;
  }
  .crop-marks {
    position: absolute;
    inset: 0;
  }
  .origin-line {
    position: absolute;
    top: 122px;
    left: 0;
    width: 1200px;
    display: flex;
    justify-content: center;
    align-items: center;
    gap: 18px;
    font-family: "Arimo", sans-serif;
    font-size: 24px;
    color: var(--ink-soft);
  }
  .flag-badge {
    width: 84px;
    height: 84px;
    border-radius: 50%;
    background: radial-gradient(circle at 50% 50%, var(--flag-white) 0 30%, var(--flag-red) 31% 100%);
    box-shadow: 0 2px 4px rgba(0,0,0,0.25);
    margin-top: -8px;
  }
  .brand-name {
    position: absolute;
    top: 200px;
    left: 0;
    width: 1200px;
    height: 258px;
    margin: 0;
    display: flex;
    justify-content: center;
    align-items: center;
    font-family: "Arimo", sans-serif;
    font-weight: 700;
    font-size: 230px;
    line-height: 1;
    letter-spacing: -4px;
    color: var(--ink);
  }
  .service-title {
    position: absolute;
    top: 472px;
    left: 0;
    width: 1200px;
    margin: 0;
    text-align: center;
    font-family: "Alegreya SC", serif;
    font-weight: 800;
    font-size: 64px;
    line-height: 1;
    color: var(--ink);
  }
  .experience-tagline {
    position: absolute;
    top: 552px;
    left: 0;
    width: 1200px;
    margin: 0;
    text-align: center;
    font-family: "Pinyon Script", cursive;
    font-size: 48px;
    line-height: 1;
    color: var(--ink);
  }
</style>
</head>
<body>
  <main class="card">
    <svg class="crop-marks" width="1200" height="750" viewBox="0 0 1200 750" aria-hidden="true">
      <g stroke="var(--crop)" stroke-width="2">
        <line x1="76" y1="0" x2="76" y2="57"/>
        <line x1="0" y1="78" x2="60" y2="78"/>
        <line x1="1128" y1="0" x2="1128" y2="57"/>
        <line x1="1146" y1="78" x2="1200" y2="78"/>
        <line x1="0" y1="675" x2="54" y2="675"/>
        <line x1="76" y1="696" x2="76" y2="750"/>
        <line x1="1146" y1="675" x2="1200" y2="675"/>
        <line x1="1128" y1="696" x2="1128" y2="750"/>
      </g>
    </svg>

    <div class="origin-line">
      <span class="origin-word">Proudly</span>
      <span class="flag-badge" role="img" aria-label="Round Canadian flag button"></span>
      <span class="origin-word">Canadian</span>
    </div>

    <h1 class="brand-name">MP7</h1>

    <p class="service-title">Food Service Representation</p>

    <p class="experience-tagline">Over years of Foodservice experience</p>
  </main>
</body>
</html>
```